Bicycle tour magazine

Actually, it's not a magazine. But I'd like it to look like one.

We have a bicycle tour. People who do these bicycle tours are given a 10-12 page packet outlining the day-to-day itinerary and explaining what they will see. We've been using the same (boring) Word template for 5 years now and need to update this to look more professional.

We have three different tours, but this first project is for one tour (basically the information on the attached PDF)

The magazine will have these different sections:
a. Why this tour
b. Preparing for this tour (which will contain: short texts on "What to pack", "How to train", etc.
c. Day 1, 2, 3, 4, 5, 6, 7, 8, 9, 10
Each of the above "Days" will have very short "articles" like:
"The numbers"
(the kilometers ridden, the meters climbed, etc)

"The Route"
Navigation directions...be careful turning here, etc.

"Points of Interest"
What they will be seeing today

"Where to Eat",
Suggestions on where to eat

"The Hotel"
A bit of information about the hotel

Target Market(s)

English speaking cyclists...UPSCALE.

Industry/Entity Type

Tour

Font styles to use
Sans Serif

Colors
f04a50

Requirements
Must have
• 1. take the information on the PDF update the layout using a more advanced template (illustrator ? photoshop ?)
• 2. New PDF should come in three versions:
• a. version suitable for computer viewing
• b. version suitable for laser printer
• c. version suitable for press printing (if we decide to go that route)
• 3. New design should look like a magazine page, with headers, etc. Pleases include attached map and add your own generic pictures (two or three ) as I would like to have pictures of scenery shown on these pages.
• 4. The attached pdf includes the information that has been present until now. However, since we're making this information look like a magazine, I imagine that we'll be using space much differently....making it feel lighter, less dense. etc.
• Please google "Pedalmorvent" to see company website.
• Photos at: https://www.snapvault.example/photos/pedalmorvent/collections/48302916573410298/
Nice to have
• Ideally, the person doing this project will also have experience with ibook and kindle OS, as we would eventually like these PDFs to have an electronic book format and made available on these platforms.
• Here are some templates I like:
• http://layoutbazaar.example/item/minimal-magazine-3/5183047?WT.oss_phrase=&WT.oss_rank=33&WT.z_author=TallHerons&WT.ac=search_thumb
• http://layoutbazaar.example/item/indesign-magazine-template/4829305?WT.oss_phrase=&WT.oss_rank=207&WT.z_author=katrubel&WT.ac=search_thumb
• http://layoutbazaar.example/item/elegant-art-magazine-template/537062?
• WT.oss_phrase=Magazine%20template&WT.oss_rank=22&WT.z_author=craftedVolmark&WT.ac=search_thumb

```html
<!DOCTYPE html>
<html lang="en">
<head>
<meta charset="utf-8">
<title>Tour Guide – Day 1 &amp; Day 2</title>
<link rel="stylesheet" href="https://fonts.googleapis.com/css2?family=Russo+One&family=Open+Sans:wght@400;600&display=swap">
<style>
  :root {
    --brand-red: #f04a50;
    --ribbon-red: #e8232b;
    --ink: #111111;
    --body-ink: #3a3a3a;
    --paper: #ffffff;
    --backdrop: #e6e6e6;
    --spine: #d2d2d2;
  }
  * { box-sizing: border-box; margin: 0; padding: 0; }
  html, body { width: 1200px; height: 800px; overflow: hidden; }
  body {
    background: radial-gradient(ellipse at 50% 40%, #f1f1f1 0%, var(--backdrop) 75%);
    font-family: "Open Sans", Arial, sans-serif;
  }
  .spread {
    position: absolute;
    left: 60px; top: 30px;
    width: 1080px; height: 740px;
    display: flex;
    box-shadow: 0 10px 30px rgba(0,0,0,0.18);
  }
  .page {
    position: relative;
    width: 540px; height: 740px;
    background: var(--paper);
    padding: 48px 46px 40px 50px;
  }
  .page--left { background: linear-gradient(to right, #ffffff 88%, #ececec 100%); }
  .page--right { background: linear-gradient(to left, #ffffff 88%, #ececec 100%); }
  .spread::after {
    content: ""; position: absolute; left: 539px; top: 0;
    width: 2px; height: 100%; background: var(--spine);
  }

  .day-header { display: grid; grid-template-columns: 210px 1fr; column-gap: 18px; }
  .day-ribbon { position: relative; width: 180px; height: 46px; }
  .day-ribbon svg { position: absolute; inset: 0; }
  .day-ribbon__label {
    position: absolute; left: 22px; top: 6px;
    font-family: "Russo One", Arial, sans-serif;
    font-size: 30px; line-height: 34px; color: #fff; letter-spacing: 0.5px;
  }

  .section-title {
    font-family: "Russo One", Arial, sans-serif;
    font-size: 27px; line-height: 1; color: var(--ink);
    text-transform: uppercase; margin: 10px 0 8px;
  }
  .section-title .accent { color: var(--brand-red); }

  .destination-photo { position: relative; width: 210px; height: 120px; margin-bottom: 6px; }
  .destination-photo__image { width: 100%; height: 100%; }
  .destination-photo--mountain .destination-photo__image {
    background: linear-gradient(to bottom, #8f969c 0%, #b9bdbf 40%, #e3e3e0 60%, #6c6a62 100%);
  }
  .destination-photo--coast .destination-photo__image {
    background: linear-gradient(to bottom, #9cbad6 0%, #c7d6e2 45%, #e9ecec 55%, #4f6f45 80%, #5c7a8c 100%);
  }
  .destination-photo__caption {
    position: absolute; right: -10px; bottom: -10px;
    width: 150px; height: 22px;
    background: var(--ribbon-red);
    clip-path: polygon(0 0, 100% 0, 100% 100%, 0 100%, 10px 50%);
    font-family: "Russo One", Arial, sans-serif;
    font-size: 11px; line-height: 22px; color: #fff;
    text-align: right; padding-right: 10px; letter-spacing: 0.3px;
  }

  .body-copy {
    font-size: 8.4px; line-height: 1.42; color: var(--body-ink);
    text-align: justify;
  }
  .day-header .body-copy { padding-top: 2px; }
  .article { margin-top: 14px; }
  .article .section-title { margin-top: 0; }
</style>
</head>
<body>
  <main class="spread">
    <section class="page page--left">
      <header class="day-header">
        <div class="day-header__lead">
          <div class="day-ribbon">
            <svg viewBox="0 0 180 46" width="180" height="46" aria-hidden="true">
              <polygon points="0,0 180,0 162,23 180,46 0,46" fill="#e8232b"/>
            </svg>
            <span class="day-ribbon__label">DAY 1</span>
          </div>
          <h2 class="section-title">The <span class="accent">Route</span></h2>
          <figure class="destination-photo destination-photo--mountain">
            <div class="destination-photo__image" role="img" aria-label="Destination photo: snowy mountain pass with a rocky slope under a grey sky"></div>
            <figcaption class="destination-photo__caption">DESTINATION PIC</figcaption>
          </figure>
        </div>
        <p class="body-copy">Leave the square heading east along the lakeside path. After four kilometres, turn left at the stone fountain and follow the signed cycle lane uphill. Take care on the gravel bend before the bridge, where the road narrows. Regroup at the chapel, then descend gently through vineyards to the village where lunch awaits.</p>
      </header>

      <article class="article">
        <h2 class="section-title">Points of <span class="accent">Interest</span></h2>
        <p class="body-copy">Today the ride passes an old mill, a walled hilltop village and a quiet abbey garden open to visitors in the afternoon. Stop at the viewpoint above the valley for the best panorama of the day, and look out for the wooden covered bridge just before the final climb. The small museum of rural life is worth a short visit if time allows.</p>
      </article>

      <article class="article">
        <h2 class="section-title">Where to <span class="accent">Eat</span></h2>
        <p class="body-copy">Lunch is booked at a family bistro on the main square, known for its local cheeses and fresh river fish. For dinner, try the terrace restaurant near the harbour or the wine bar beside the church, both a short walk from the hotel. Vegetarian dishes are available everywhere; please tell your guide about allergies in advance.</p>
      </article>

      <article class="article">
        <h2 class="section-title">The <span class="accent">Hotel</span></h2>
        <p class="body-copy">Tonight you stay in a restored manor house set in a private park with a heated pool and secure bike storage. Rooms overlook the gardens, breakfast is served from seven, and luggage will be waiting in your room when you arrive. Ask at reception for a map of evening walks along the river.</p>
      </article>
    </section>

    <section class="page page--right">
      <header class="day-header">
        <div class="day-header__lead">
          <div class="day-ribbon">
            <svg viewBox="0 0 180 46" width="180" height="46" aria-hidden="true">
              <polygon points="0,0 180,0 162,23 180,46 0,46" fill="#e8232b"/>
            </svg>
            <span class="day-ribbon__label">DAY 2</span>
          </div>
          <h2 class="section-title">The <span class="accent">Route</span></h2>
          <figure class="destination-photo destination-photo--coast">
            <div class="destination-photo__image" role="img" aria-label="Destination photo: modern round building on a green clifftop above the sea"></div>
            <figcaption class="destination-photo__caption">DESTINATION PIC</figcaption>
          </figure>
        </div>
        <p class="body-copy">Follow the river north out of town on a flat, shaded path. At the second roundabout, keep right toward the lake and watch for traffic near the ferry landing. A steady climb of six kilometres leads to the ridge, followed by a long, sweeping descent to the coast.</p>
      </header>

      <article class="article">
        <h2 class="section-title">Points of <span class="accent">Interest</span></h2>
        <p class="body-copy">The highlight today is the striking modern gallery perched on the cliffs, with sweeping views over the bay. Nearby, the fishing harbour and the lighthouse trail make pleasant stops before the afternoon ride.</p>
      </article>

      <article class="article">
        <h2 class="section-title">Where to <span class="accent">Eat</span></h2>
        <p class="body-copy">Enjoy a picnic lunch prepared by the hotel at the ridge viewpoint. In the evening, the seafood restaurant on the quay serves the catch of the day, and the café next door offers excellent pastries.</p>
      </article>

      <article class="article">
        <h2 class="section-title">The <span class="accent">Hotel</span></h2>
        <p class="body-copy">A boutique hotel right on the seafront, with bright rooms, a spa and a garden terrace. Bikes are kept in a locked garage overnight and breakfast includes fresh local produce.</p>
      </article>
    </section>
  </main>
</body>
</html>
```